Radon Reduction & Mold Removal Website

I need you to set up a WordPress account for me and design a full width, professional-looking, mobile-responsive website for my business. We offer radon reduction and mold removal (two household environmental issues).
We have merged 2 companies and need a single website to promote both services (radon and mold). Here are the current websites from the 2 businesses that have merged:
RADON
http://klendor-airfix.com/
MOLD
http://brisketfungusclear.net/
Once complete, I will need the login to the WordPress account so I have access to the site to make changes, additions, and modifications.
Target Market(s)
Home Owners
Industry/Entity Type
Home And Garden
Look and feel
Each slider illustrates characteristics of the customer's brand and the style your logo design should communicate.

```html
<!DOCTYPE html>
<html lang="en">
<head>
<meta charset="utf-8">
<title>Klendor Airfix – Radon Mitigation &amp; Mold Removal</title>
<link href="https://fonts.googleapis.com/css2?family=Oswald:wght@400;500;700&family=Open+Sans:wght@400;600;700&display=swap" rel="stylesheet">
<style>
:root{
  --green:#3f9b1f;
  --green-dark:#2c7a12;
  --lime:#c9d62b;
  --yellow:#e9e41d;
  --ink:#222;
  --text:#555;
  --grey-band:#eeeeee;
  --footer:#2e2e2e;
  --footer-bottom:#1f1f1f;
  --white:#fff;
}
*{box-sizing:border-box;margin:0;padding:0}
html,body{width:1200px;height:2663px;overflow:hidden}
body{font-family:"Open Sans",Arial,sans-serif;color:var(--text);background:var(--white);position:relative}
.section{position:absolute;left:0;width:1200px}
.btn-yellow{display:inline-block;background:var(--yellow);color:var(--ink);font-family:"Oswald",sans-serif;font-weight:500;font-size:17px;padding:8px 22px;border-radius:18px}
.btn-more{display:inline-block;border:1px solid #bbb;border-radius:14px;padding:4px 20px;font-size:13px;font-weight:600;color:#333;background:#fff}

/* header + hero */
.hero{top:0;height:485px}
.hero-photo{position:absolute;inset:0;background:linear-gradient(180deg,#3a3a36 0%,#4a4a44 40%,#2e2f2a 100%)}
.hero-shade{position:absolute;inset:0;background:rgba(0,0,0,.35)}
.brand{position:absolute;left:110px;top:22px;font-family:"Oswald",sans-serif;font-weight:700;font-size:34px;color:var(--yellow);letter-spacing:1px}
.top-phone{position:absolute;right:130px;top:14px;color:#ddd;font-size:14px}
.top-phone b{font-family:"Oswald",sans-serif;font-weight:500;color:var(--lime);font-size:22px;margin-left:6px}
.nav{position:absolute;left:570px;top:64px;display:flex;gap:22px;list-style:none}
.nav li{font-family:"Oswald",sans-serif;font-size:14px;color:#fff;padding:5px 16px}
.nav li.active{border:2px solid var(--green);border-radius:16px}
.hero-title{position:absolute;top:240px;width:100%;text-align:center;font-family:"Oswald",sans-serif;font-weight:500;font-size:40px;color:#fff;letter-spacing:1px}
.hero-sub{position:absolute;top:304px;left:190px;width:820px;text-align:center;color:#eee;font-size:13px;line-height:20px}
.hero-cta{position:absolute;top:362px;width:100%;text-align:center}
.hero-arrow{position:absolute;top:290px}

/* search */
.search{top:485px;height:95px;background:linear-gradient(180deg,#d3de3c,#b6c61f)}
.search label{position:absolute;top:12px;font-size:17px;color:#333}
.search .field{position:absolute;top:40px;height:38px;background:#fff;border:1px solid #ccc;font-size:12px;color:#aaa;padding:11px 10px}
.search .go{position:absolute;left:920px;top:40px;width:126px;height:38px;background:#111;color:#fff;font-family:"Oswald",sans-serif;font-size:18px;display:flex;align-items:center;justify-content:center;gap:8px}

/* intro */
.intro{top:580px;height:233px;text-align:center}
.intro h2{margin-top:32px;font-family:"Oswald",sans-serif;font-weight:400;font-size:32px;color:var(--ink)}
.intro h2 span{color:var(--green)}
.intro p{width:900px;margin:18px auto 0;font-size:12.5px;line-height:20px}
.intro .btn-more{margin-top:16px}

/* fix band */
.fix{top:813px;height:121px;background:#111}
.fix-tag{position:absolute;left:0;top:0;width:300px;height:121px;background:var(--green);clip-path:polygon(0 0,100% 0,88% 100%,0 100%)}
.fix-tag h3{position:absolute;left:140px;top:20px;font-family:"Oswald",sans-serif;font-weight:500;font-size:27px;line-height:38px;color:#fff}
.fix p{position:absolute;left:310px;top:22px;width:560px;color:#fff;font-size:16px;line-height:26px}
.fix-phone{position:absolute;left:885px;top:44px;display:flex;align-items:center;gap:10px;font-family:"Oswald",sans-serif;font-size:26px;color:var(--lime)}

/* services */
.services{top:934px;height:152px;background:var(--grey-band)}
.service{position:absolute;top:27px;width:320px}
.service .icon{position:absolute;left:0;top:0;width:96px;height:96px;border-radius:50%;background:#fff;box-shadow:0 2px 6px rgba(0,0,0,.15);display:flex;align-items:center;justify-content:center}
.service h4{position:absolute;left:104px;top:4px;font-family:"Oswald",sans-serif;font-weight:400;font-size:21px;line-height:24px;color:#333}
.service h4 em{font-style:normal;color:var(--green)}
.service p{position:absolute;left:104px;top:58px;width:212px;font-size:11.5px;line-height:17px}

/* news */
.news{top:1089px;height:356px}
.video{position:absolute;left:110px;top:38px;width:523px;height:282px;background:linear-gradient(135deg,#3a3a3a,#1a1a1a)}
.video-bar{position:absolute;left:0;bottom:0;width:100%;height:28px;background:#0c0c0c}
.news h3{position:absolute;left:660px;top:32px;width:440px;font-family:"Oswald",sans-serif;font-weight:400;font-size:30px;line-height:36px;color:var(--green)}
.news p{position:absolute;left:660px;width:430px;font-size:12.5px;line-height:19px}
.news .btn-more{position:absolute;left:660px;top:278px}

/* what is radon */
.radon{top:1445px;height:330px;text-align:center}
.radon-photo{position:absolute;inset:0;background:linear-gradient(180deg,#4fae28 0%,#3a9318 60%,#2f7f12 100%)}
.radon h2{position:relative;margin-top:40px;font-family:"Oswald",sans-serif;font-weight:400;font-size:34px;color:#fff}
.radon p{position:relative;width:980px;margin:14px auto 0;font-size:12.5px;line-height:20px;color:#eaf6e0}
.radon .btn-yellow{position:relative;margin-top:26px}

/* gallery */
.gallery{top:1775px;height:289px;text-align:center}
.gallery h2{margin-top:28px;font-family:"Oswald",sans-serif;font-weight:400;font-size:34px;color:var(--ink)}
.gallery h2 span{color:var(--green)}
.thumb{position:absolute;top:90px;width:186px;height:162px;padding:8px;background:#fff;box-shadow:0 2px 8px rgba(0,0,0,.25)}
.thumb div{width:100%;height:100%}
.g-arrow{position:absolute;top:140px}

/* partners */
.partners{top:2064px;height:284px;background:linear-gradient(180deg,#3f9b1f,#2f8414)}
.partners p{width:980px;margin:30px auto 0;text-align:center;color:#fff;font-size:12.5px;line-height:20px}
.badge{position:absolute;top:134px;height:106px;background:#fff;display:flex;align-items:center;justify-content:center;box-shadow:0 2px 6px rgba(0,0,0,.25)}

/* footer */
.footer{top:2348px;height:271px;background:var(--footer);color:#bbb}
.f-col{position:absolute;top:24px}
.f-col h5{font-family:"Oswald",sans-serif;font-weight:400;font-size:20px;color:#eee;margin-bottom:16px}
.f-col p{font-size:12.5px;line-height:19px}
.f-col .quote-head{color:var(--lime);font-weight:600}
.news-input{width:240px;height:30px;background:#fff;font-size:11px;color:#999;padding:7px 10px;margin:6px 0 10px}
.sign{display:inline-block;background:var(--yellow);color:#222;font-family:"Oswald",sans-serif;font-size:16px;padding:4px 14px}
.row{display:flex;align-items:center;gap:8px;font-size:12.5px;margin-bottom:10px}
.bottom{top:2619px;height:44px;background:var(--footer-bottom);color:#999;font-size:11.5px}
.bottom .links{position:absolute;left:110px;top:14px;display:flex;gap:20px}
.bottom .copy{position:absolute;right:110px;top:14px}
</style>
</head>
<body>

<header class="section hero">
  <div class="hero-photo" role="img" aria-label="Townhouse facade with a radon mitigation fan and piping on the exterior wall"></div>
  <div class="hero-shade"></div>
  <div class="brand">KLENDOR AIRFIX</div>
  <div class="top-phone">Radon &amp; Mold : <b>1-800-555-0142</b></div>
  <ul class="nav">
    <li class="active">HOME</li><li>SERVICES</li><li>CONTACT</li><li>PRODUCTS</li><li>GET A QUOTE</li>
  </ul>
  <svg class="hero-arrow" style="left:110px" width="30" height="60" viewBox="0 0 30 60"><polyline points="24,4 6,30 24,56" fill="none" stroke="#bbb" stroke-width="3"/></svg>
  <svg class="hero-arrow" style="right:110px" width="30" height="60" viewBox="0 0 30 60"><polyline points="6,4 24,30 6,56" fill="none" stroke="#bbb" stroke-width="3"/></svg>
  <h1 class="hero-title">PROTECT WHAT'S IMPORTANT</h1>
  <p class="hero-sub">Klendor Airfix is the best choice for radon mitigation and mold removal for your home or business. Radon is the number one cause of lung cancer among non-smokers, and hidden mold harms the air your family breathes every day.</p>
  <div class="hero-cta"><span class="btn-yellow">GET A QUOTE !</span></div>
</header>

<section class="section search">
  <label style="left:118px">Address</label>
  <label style="left:518px">Radius</label>
  <div class="field" style="left:115px;width:385px">City, State</div>
  <div class="field" style="left:515px;width:395px">City, State</div>
  <div class="go">
    <svg width="16" height="16" viewBox="0 0 16 16"><circle cx="6.5" cy="6.5" r="5" fill="none" stroke="#fff" stroke-width="2"/><line x1="10" y1="10" x2="15" y2="15" stroke="#fff" stroke-width="2"/></svg>
    SEARCH
  </div>
</section>

<section class="section intro">
  <h2>Radon Mitigation and <span>Mold Removal</span></h2>
  <p>High levels of radon have been found in every state across America, and mold grows wherever moisture is left unchecked. Radon mitigation, radon testing and mold removal have become more prevalent in residential, commercial and real-estate environments, with the real-estate market showing the biggest growth due to state and local regulations on homes for sale.</p>
  <span class="btn-more">More</span>
</section>

<section class="section fix">
  <div class="fix-tag"><h3>FIX YOUR<br>HOME TODAY</h3></div>
  <p>Radon and mold company helping resolve your indoor air issues. We reduce your radon levels and remove mold from your home so you will be safe and healthy</p>
  <div class="fix-phone">
    <svg width="18" height="28" viewBox="0 0 18 28"><rect x="1" y="1" width="16" height="26" rx="3" fill="none" stroke="#ccc" stroke-width="2"/><line x1="6" y1="23" x2="12" y2="23" stroke="#ccc" stroke-width="2"/></svg>
    1-800-555-0142
  </div>
</section>

<section class="section services">
  <div class="service" style="left:110px">
    <div class="icon"><svg width="40" height="40" viewBox="0 0 40 40"><polygon points="20,6 4,20 9,20 9,34 31,34 31,20 36,20" fill="#444"/><rect x="17" y="24" width="6" height="10" fill="#fff"/></svg></div>
    <h4><em>RESIDENTIAL</em><br>SERVICES</h4>
    <p>Certified radon and mold technicians for every home.</p>
  </div>
  <div class="service" style="left:433px">
    <div class="icon"><svg width="40" height="40" viewBox="0 0 40 40"><rect x="10" y="6" width="20" height="28" fill="#444"/><g fill="#fff"><rect x="14" y="10" width="4" height="4"/><rect x="22" y="10" width="4" height="4"/><rect x="14" y="18" width="4" height="4"/><rect x="22" y="18" width="4" height="4"/><rect x="18" y="27" width="4" height="7"/></g></svg></div>
    <h4><em>COMMERCIAL</em><br>SERVICES</h4>
    <p>Radon reduction and mold removal for any business.</p>
  </div>
  <div class="service" style="left:769px">
    <div class="icon"><svg width="40" height="40" viewBox="0 0 40 40"><polygon points="20,5 5,18 35,18" fill="none" stroke="#444" stroke-width="2.5"/><rect x="9" y="18" width="22" height="16" fill="none" stroke="#444" stroke-width="2.5"/><text x="20" y="31" text-anchor="middle" font-family="Open Sans,sans-serif" font-size="12" font-weight="700" fill="#444">$</text></svg></div>
    <h4><em>REAL ESTATE</em><br>SERVICES</h4>
    <p>Fast radon and mold checks before every home sale.</p>
  </div>
</section>

<section class="section news">
  <div class="video" role="img" aria-label="Video still of a technician fitting white radon vent pipe">
    <svg style="position:absolute;left:236px;top:112px" width="52" height="52" viewBox="0 0 52 52"><circle cx="26" cy="26" r="24" fill="rgba(0,0,0,.5)" stroke="#ddd" stroke-width="2"/><polygon points="20,15 38,26 20,37" fill="#ddd"/></svg>
    <div class="video-bar">
      <svg width="523" height="28" viewBox="0 0 523 28"><polygon points="10,8 20,14 10,20" fill="#ccc"/><rect x="32" y="12" width="330" height="4" fill="#444"/><rect x="32" y="12" width="40" height="4" fill="#888"/><text x="375" y="18" font-family="Open Sans,sans-serif" font-size="10" fill="#aaa">00:00:00</text><rect x="440" y="9" width="14" height="10" fill="none" stroke="#aaa"/><rect x="470" y="12" width="40" height="4" fill="#888"/></svg>
    </div>
  </div>
  <h3>Nonsmoking woman believes radon caused her lung cancer</h3>
  <p style="top:118px">BELLVILLE, OH (WKLX) - It is the number one cause of lung cancer in nonsmokers and it could be in your house. One woman believes radon in her home made her sick.</p>
  <p style="top:184px">Warning about radon levels in homes One thing becomes quickly clear when a radon reduction system is being installed, everything must be tightly sealed for it to work properly, according to removal expert Dale Ferrin. He installed a system in Nina and Pete Varrow's home.</p>
  <span class="btn-more">More</span>
</section>

<section class="section radon">
  <div class="radon-photo" role="img" aria-label="Green toned photo of a house exterior with radon vent piping"></div>
  <h2>What is Radon?</h2>
  <p>Radon is everywhere indoor and outdoor with the higher levels being found indoor where radon is more concentrated and takes longer to break down. Radon is a radioactive gas that is caused by the decay of uranium in the soil. Radon gas is a colorless, odorless, and invisible gas that can only be detected by radon testing. Radon gas penetrates most common building materials and is fairly soluble in water. Exposure to radon is most common through ingestion and inhalation, with inhalation being the largest threat to your health. Radon awareness has grown exponentially over the past 10 years and is now becoming a more common issue nationwide. Visit our radon and mold information pages to learn more about the dangers of radon gas and mold and what you can do to keep everyone safe.</p>
  <span class="btn-yellow">GET A QUOTE !</span>
</section>

<section class="section gallery">
  <h2>Photo <span>Gallery</span></h2>
  <svg class="g-arrow" style="left:108px" width="22" height="60" viewBox="0 0 22 60"><polyline points="18,4 4,30 18,56" fill="none" stroke="#ccc" stroke-width="3"/></svg>
  <svg class="g-arrow" style="right:108px" width="22" height="60" viewBox="0 0 22 60"><polyline points="4,4 18,30 4,56" fill="none" stroke="#ccc" stroke-width="3"/></svg>
  <div class="thumb" style="left:150px"><div role="img" aria-label="Exterior radon pipe along a house wall" style="background:linear-gradient(135deg,#6b6b63,#b9b4a6)"></div></div>
  <div class="thumb" style="left:382px"><div role="img" aria-label="Radon pipe installed in a basement corner" style="background:linear-gradient(135deg,#8c4b36,#c98a6c)"></div></div>
  <div class="thumb" style="left:601px"><div role="img" aria-label="White radon fan and pipe fittings" style="background:linear-gradient(135deg,#6d6d6d,#d5d5d5)"></div></div>
  <div class="thumb" style="left:826px"><div role="img" aria-label="Radon vent running up a two storey house" style="background:linear-gradient(180deg,#6f8fc0,#b59b7a)"></div></div>
</section>

<section class="section partners">
  <p>Klendor Airfix is quickly becoming a household name across the United States. Offering radon reduction and mold removal in over forty locations across America has made us the golden standard for healthy indoor air. We were not always such a large company, and actually started from very humble beginnings. We began in 1988 with only one specialist. Now we boast a team of over 100 employees, and have experienced tremendous growth over the past ten years! As we continue to grow we strive to keep our quality of work to the same standard.</p>
  <div class="badge" style="left:116px;width:124px"><svg width="90" height="60"><rect x="5" y="5" width="80" height="50" rx="6" fill="#d9d9d9"/></svg></div>
  <div class="badge" style="left:284px;width:124px"><svg width="90" height="60"><rect x="10" y="8" width="70" height="44" fill="#d9d9d9"/></svg></div>
  <div class="badge" style="left:451px;width:129px"><svg width="80" height="80"><circle cx="40" cy="40" r="34" fill="#d9d9d9"/></svg></div>
  <div class="badge" style="left:632px;width:160px"><svg width="120" height="50"><rect x="5" y="8" width="110" height="34" fill="#d9d9d9"/></svg></div>
  <div class="badge" style="left:826px;width:219px"><svg width="170" height="70"><rect x="5" y="8" width="160" height="54" rx="8" fill="#d9d9d9"/></svg></div>
</section>

<footer class="section footer">
  <div class="f-col" style="left:110px;width:220px">
    <h5>Client Testimonial</h5>
    <p class="quote-head">... Out Standing ...</p>
    <p>Klendor Airfix cleared our radon and mold problems fast and left the house spotless ...</p>
    <p style="color:var(--lime);margin-top:8px">Lorin P</p>
  </div>
  <div class="f-col" style="left:366px;width:250px">
    <h5>Newsletter Signup</h5>
    <p>Mail id :</p>
    <div class="news-input">Enter your email here</div>
    <span class="sign">Sign up</span>
  </div>
  <div class="f-col" style="left:632px;width:230px">
    <h5>Contact Us</h5>
    <p style="color:#ddd;margin-bottom:8px">Corporate Headquarters</p>
    <div class="row"><svg width="12" height="14" viewBox="0 0 12 14"><rect x="2" y="1" width="8" height="12" rx="1.5" fill="#bbb"/></svg>1-800-555-0142</div>
    <div class="row"><svg width="14" height="10" viewBox="0 0 14 10"><rect x="0.5" y="0.5" width="13" height="9" fill="none" stroke="#bbb"/><polyline points="0.5,0.5 7,6 13.5,0.5" fill="none" stroke="#bbb"/></svg>info@klendorairfix.com</div>
  </div>
  <div class="f-col" style="left:864px;width:230px">
    <h5>Opening hours</h5>
    <div class="row"><svg width="12" height="12"><circle cx="6" cy="6" r="5" fill="none" stroke="#bbb"/><polyline points="6,3 6,6 8,7" fill="none" stroke="#bbb"/></svg>Mon - Fri : 7am - 8pm</div>
    <div class="row"><svg width="12" height="12"><circle cx="6" cy="6" r="5" fill="none" stroke="#bbb"/><polyline points="6,3 6,6 8,7" fill="none" stroke="#bbb"/></svg>Sat : 8am - 5pm</div>
  </div>
</footer>

<div class="section bottom">
  <div class="links"><span>Terms of Use</span><span>Privacy Policy</span><span>Directory</span></div>
  <div class="copy">Copyright © 2015 Radon Mitigation &amp; Mold Removal | Klendor Airfix Mitigation Services</div>
</div>

</body>
</html>
```